Webdesign (Portalskonzept und -design) für Online-Portal
Zielgruppe
Mit KOMPASS (www.kompassjournal-beispiel.ch) besteht ein starker Brand in der Ostschweiz für ein Magazin, dass monatlich an über 8'000 CEO’s (Kader) der Ostschweiz per Post versendet wird. Aktuelle News sind auf dem Portal von KOMPASS online aufgeschaltet und werden via Newsletter versendet. Der Brand KOMPASS ist in der Ostschweiz bekannt und etabliert. Nun soll der Offline-Brand für die digitale Zukunft gerüstet werden.
Aufgabenstellung
Entwicklung modernes Portaldesign (Webseite) in responsive / mobile first => www.kompassnetz-beispiel.ch
Ziel; Es soll ein Online-Portal unter dem Brand kompassnetz-beispiel.ch aufgebaut werden. Auf diesem Portal integriert werden die News (kompassjournal-beispiel.ch) sowie weitere Unterrubriken wie z.B. Jobs, Events, etc.
Beispiel: KOMPASStalk, KOMPASSjobs, KOMPASSevent, etc.
Der bestehende Brand KOMPASS (offline) muss dabei zwingender Bestandteil zur Wiedererkennung sein und darf nicht verändert sondern nur ergänzt werden. Das Portal kann man sich vorstellen wie vergleicho-beispiel.de – eine laufende Erweiterung um weitere Rubriken soll möglich sein. Der Brand / das Logo darf für KOMPASSDigital 'erweitert' werden.
Das Design soll modern & schlank wirken sowie primär für Mobilgeräte (mobile first) gestaltet sein.
Bei http://www.medinetz-seite-beispiel.de/index.php finden wir die 2. Navigations-Ebene interessant umgesetzt. Mit besseren Symbolen könnte das eine gute Art sein.
Vom Look & Feel gefällt https://www.wirtschaftsblick-beispiel.ch (Startseite für News)

```html
<!DOCTYPE html>
<html lang="de">
<head>
<meta charset="utf-8">
<title>KOMPASS digital – Startseite</title>
<link href="https://fonts.googleapis.com/css2?family=Roboto+Condensed:wght@400;700&family=Roboto:wght@400;500;700&display=swap" rel="stylesheet">
<style>
  :root {
    --brand-red: #8c1c22;
    --page-grey: #eeeeee;
    --paper: #ffffff;
    --ink: #1d1d1d;
    --muted: #8a8a8a;
    --rule: #e2e2e2;
    --job-bg: #f6f6f6;
  }
  * { box-sizing: border-box; margin: 0; padding: 0; }
  html, body { width: 1200px; height: 800px; overflow: hidden; }
  body { background: var(--page-grey); font-family: "Roboto", sans-serif; color: var(--ink); position: relative; }

  .site-header { position: absolute; left: 0; top: 0; width: 1200px; height: 120px; background: var(--brand-red); }
  .brand { position: absolute; left: 66px; top: 30px; color: #fff; font-family: "Roboto Condensed", sans-serif; font-weight: 700; font-size: 36px; letter-spacing: 1px; line-height: 1; }
  .search { position: absolute; right: 66px; top: 40px; width: 210px; height: 28px; background: #fff; border: 1px solid #d6d6d6; }
  .search svg { position: absolute; right: 8px; top: 7px; }

  .page { position: absolute; left: 44px; top: 96px; width: 1112px; height: 704px; background: var(--paper); overflow: hidden; }
  .dateline { position: absolute; right: 24px; top: 22px; font-size: 9px; color: var(--muted); letter-spacing: .3px; }
  .main-nav { position: absolute; left: 24px; top: 54px; display: flex; gap: 28px; font-weight: 500; font-size: 13px; color: var(--brand-red); }
  .share { position: absolute; right: 24px; top: 56px; display: flex; gap: 12px; }
  .share span { width: 10px; height: 10px; border-radius: 50%; background: #d2d2d2; display: block; }
  .nav-rule { position: absolute; left: 24px; right: 24px; top: 84px; border-top: 1px solid var(--rule); }

  .tile { position: absolute; overflow: hidden; }
  .tile-media { position: absolute; inset: 0; }
  .tile-text { position: absolute; left: 20px; right: 20px; bottom: 16px; color: #fff; }
  .tag { display: inline-block; background: var(--brand-red); color: #fff; font-family: "Roboto Condensed", sans-serif; font-weight: 700; font-size: 10px; padding: 3px 6px; margin-bottom: 8px; }
  .tile-title { font-family: "Roboto Condensed", sans-serif; font-weight: 700; font-size: 20px; line-height: 1.2; }
  .hero .tile-title { font-size: 26px; }
  .tile-lead { font-size: 12px; line-height: 1.3; margin-top: 8px; color: #eee; }
  .dots { position: absolute; left: 18px; top: 14px; display: flex; gap: 5px; }
  .dots span { width: 5px; height: 5px; border-radius: 50%; background: var(--brand-red); }

  .hero { left: 24px; top: 114px; width: 610px; height: 350px; }
  .talk { left: 646px; top: 114px; width: 250px; height: 168px; }
  .news { left: 646px; top: 294px; width: 250px; height: 170px; }
  .ad { left: 908px; top: 114px; width: 180px; height: 246px; }

  .card { position: absolute; top: 478px; }
  .card-media { position: relative; height: 122px; }
  .card-date { position: absolute; left: 0; bottom: 0; background: var(--brand-red); color: #fff; font-size: 10px; padding: 4px 8px; }
  .card-title { font-family: "Roboto Condensed", sans-serif; font-weight: 700; font-size: 17px; color: var(--brand-red); margin-top: 12px; }
  .card-lead { font-size: 11px; color: var(--muted); margin-top: 6px; }
  .card-a { left: 24px; width: 294px; }
  .card-b { left: 330px; width: 304px; }

  .jobs { position: absolute; left: 646px; top: 478px; width: 250px; height: 226px; background: var(--job-bg); padding: 14px; }
  .jobs h3 { font-family: "Roboto Condensed", sans-serif; font-weight: 700; font-size: 18px; color: var(--brand-red); margin-bottom: 14px; }
  .job { border-top: 1px solid var(--rule); padding: 12px 0; }
  .job-company { font-size: 10px; font-style: italic; color: var(--muted); }
  .job-title { font-family: "Roboto Condensed", sans-serif; font-weight: 700; font-size: 13px; margin-top: 4px; line-height: 1.25; }
</style>
</head>
<body>
  <header class="site-header">
    <div class="brand">KOMPASS digital</div>
    <div class="search">
      <svg width="12" height="12" viewBox="0 0 12 12" aria-hidden="true"><circle cx="5" cy="5" r="3.6" fill="none" stroke="#555" stroke-width="1.4"/><line x1="7.6" y1="7.6" x2="11" y2="11" stroke="#555" stroke-width="1.6"/></svg>
    </div>
  </header>

  <main class="page">
    <div class="dateline">MONTAG 11. JUNI 2018</div>
    <nav class="main-nav">
      <span>News</span><span>Talk</span><span>Jobs</span><span>Events</span><span>Deals</span><span>Kultur</span><span>Reisen</span><span>Golf</span><span>Magazin</span><span>Reisen</span><span>Golf</span><span>Magazin</span>
    </nav>
    <div class="share"><span></span><span></span><span></span><span></span><span></span></div>
    <div class="nav-rule"></div>

    <article class="tile hero">
      <div class="tile-media" role="img" aria-label="Nachtaufnahme der beleuchteten Klosterkirche mit Festspielbühne" style="background: linear-gradient(180deg, #0d1a2e 0%, #1f4a78 45%, #0e1a2a 100%);"></div>
      <div class="dots"><span></span><span></span><span></span></div>
      <div class="tile-text">
        <span class="tag">EVENTS</span>
        <div class="tile-title">Mit dem KOMPASS an die Festspiele</div>
        <p class="tile-lead">Vom 29. Juni bis zum 13. Juli finden die Klosterhof-Festspiele auf dem Klosterhof statt. Aufgeführt wird Carlo Benvenutis Oper «Aurelio». Der KOMPASS verlost dreimal zwei Eintritte.</p>
      </div>
    </article>

    <article class="tile talk">
      <div class="tile-media" role="img" aria-label="Porträt zweier Brüder in dunkler Kleidung" style="background: linear-gradient(160deg, #3a3a3a 0%, #151515 100%);"></div>
      <div class="tile-text"><span class="tag">Talk</span><div class="tile-title">Gebrüder Reinhold im CEO Talk</div></div>
    </article>

    <article class="tile news">
      <div class="tile-media" role="img" aria-label="Porträt eines Mannes im Anzug vor hellem Hintergrund" style="background: linear-gradient(160deg, #d9d9d9 0%, #6f6f6f 55%, #1e1e1e 100%);"></div>
      <div class="tile-text"><span class="tag">News</span><div class="tile-title">St.Gallen triffts am härtesten</div></div>
    </article>

    <aside class="tile ad" role="img" aria-label="Werbebanner für eine Herbstgala des Regionalsports" style="background: linear-gradient(180deg, #2c4f8a 0%, #3b3f8f 55%, #8a2f86 100%);"></aside>

    <article class="card card-a">
      <div class="card-media" role="img" aria-label="Gesprächsrunde mit Teilnehmern" style="background: linear-gradient(120deg, #5a5f6b 0%, #2b2e36 60%, #7a1f24 100%);">
        <span class="card-date">18. Juni 2018</span>
      </div>
      <div class="card-title">Zusammenarbeit neu geregelt</div>
      <p class="card-lead">Regionale Firmen bündeln künftig ihre Kräfte</p>
    </article>

    <article class="card card-b">
      <div class="card-media" role="img" aria-label="Bühne der Award Night mit Moderatoren" style="background: linear-gradient(160deg, #1c3d6e 0%, #0c1a33 100%);">
        <span class="card-date">18. Juni 2018</span>
      </div>
      <div class="card-title">Vier OSV-Awards für die Ostschweiz</div>
      <p class="card-lead">Letzten Donnerstag fand die Award Night statt</p>
    </article>

    <section class="jobs">
      <h3>Jobangebote</h3>
      <div class="job"><div class="job-company">St. Gallen / Metallwerk Ost GmbH</div><div class="job-title">Abteilungsleiter/in Sorter und Bereitstellung</div></div>
      <div class="job"><div class="job-company">St. Gallen / Metallwerk Ost GmbH</div><div class="job-title">Abteilungsleiter/in Sorter und Bereitstellung</div></div>
    </section>
  </main>
</body>
</html>
```